Site pack insert binder cover, spine and back ART

I am looking for an insert binder design that includes varied spine widths of 48mm and 24mm, with an A4 cover and a A4 backing.
It needs to incorporate and compliment our other company related designs and be editable in Microsoft work so we can type in the general information of the site pack. Like client, address, et

Target Market(s)

Clients

Industry/Entity Type

Construction

Colors
3276b5
0455a3
85abd2

Requirements
Must have
• Microsoft word editable files

```html
<!DOCTYPE html>
<html lang="en">
<head>
<meta charset="utf-8">
<title>Kestrel Civil Projects – Site Pack Binder Cover</title>
<link rel="stylesheet" href="https://fonts.googleapis.com/css2?family=Open+Sans:wght@300;400;700;800&display=swap">
<style>
  :root {
    --stage: #404040;
    --ink: #000000;
    --paper: #ffffff;
    --brand-blue: #3f78bc;
    --brand-deep: #0455a3;
    --brand-light: #85abd2;
    --muted: #9a9a9a;
  }
  * { box-sizing: border-box; margin: 0; padding: 0; }
  html, body { width: 1200px; height: 841px; overflow: hidden; }
  body {
    position: relative;
    background: var(--stage);
    font-family: "Open Sans", Arial, sans-serif;
  }
  .panel { position: absolute; top: 141px; height: 575px; overflow: hidden; }
  .panel-label {
    position: absolute; top: 724px;
    font-size: 10px; color: #d8d8d8; letter-spacing: 0.02em;
  }

  /* Back cover */
  .back-cover { left: 97px; width: 410px; background: var(--ink); }
  .back-label { left: 289px; }
  .wordmark {
    font-weight: 800; letter-spacing: 0.02em; line-height: 1;
    display: flex; align-items: center; gap: 10px;
  }
  .wordmark-square { width: 14px; height: 14px; background: var(--brand-blue); display: block; }
  .back-cover .wordmark {
    position: absolute; left: 0; right: 0; top: 252px;
    justify-content: center; font-size: 54px; color: var(--paper);
  }
  .back-rule {
    position: absolute; left: 4px; right: 12px; top: 429px; height: 2px;
    background: linear-gradient(90deg, transparent, var(--brand-blue) 30%, var(--brand-blue) 70%, transparent);
  }
  .back-url {
    position: absolute; left: 0; right: 0; top: 442px;
    text-align: center; color: var(--paper); font-weight: 300; font-size: 18px;
  }

  /* Spine */
  .spine { left: 533px; width: 123px; background: var(--brand-blue); }
  .spine .wordmark {
    position: absolute; left: 50%; top: 50%;
    transform: translate(-50%, -50%) rotate(-90deg);
    font-size: 40px; color: var(--paper); white-space: nowrap;
  }

  /* Front cover */
  .front-cover { left: 682px; width: 410px; background: var(--paper); }
  .front-label { left: 887px; }
  .front-cover .edge-shapes { position: absolute; inset: 0; width: 410px; height: 575px; }
  .front-cover .wordmark {
    position: absolute; left: 0; right: 0; top: 138px;
    justify-content: center; font-size: 56px; color: var(--ink);
  }
  .title-block { position: absolute; left: 0; right: 0; top: 228px; text-align: center; }
  .pack-title { font-size: 38px; font-weight: 700; color: var(--brand-blue); line-height: 1.1; }
  .site-streets { font-size: 25px; font-weight: 700; color: var(--ink); line-height: 1.3; margin-top: 2px; }
  .site-suburb { font-size: 44px; font-weight: 700; color: var(--brand-blue); line-height: 1.1; margin-top: 6px; }
  .site-number { font-size: 25px; font-weight: 700; color: var(--ink); line-height: 1.1; }

  .contact-list {
    position: absolute; right: 10px; top: 481px; list-style: none;
    font-size: 8.6px; line-height: 12.2px; color: var(--ink); text-align: right;
  }
  .contact-list li { display: flex; justify-content: flex-end; align-items: center; gap: 4px; }
  .contact-list svg { width: 8px; height: 8px; fill: var(--brand-blue); flex: none; }
  .contact-list .spacer { width: 8px; flex: none; }
  .abn-tag { color: var(--brand-blue); font-weight: 700; }
</style>
</head>
<body>

  <section class="panel back-cover" aria-label="Back cover">
    <div class="wordmark"><span class="wordmark-square"></span>KESTREL</div>
    <div class="back-rule"></div>
    <p class="back-url">www.kestrelcivil.com.au</p>
  </section>
  <span class="panel-label back-label">BACK</span>

  <section class="panel spine" aria-label="Spine">
    <div class="wordmark">KESTREL</div>
  </section>

  <section class="panel front-cover" aria-label="Front cover">
    <svg class="edge-shapes" viewBox="0 0 410 575" aria-hidden="true">
      <polygon points="27,0 410,0 410,48" fill="var(--brand-blue)"/>
      <polygon points="127,20 410,56 410,68" fill="var(--ink)"/>
      <polygon points="0,532 357,575 0,575" fill="var(--brand-blue)"/>
      <polygon points="0,510 290,558 0,524" fill="var(--ink)"/>
    </svg>

    <div class="wordmark"><span class="wordmark-square"></span>KESTREL</div>

    <div class="title-block">
      <h1 class="pack-title">SITE PACK</h1>
      <p class="site-streets">HARLOW, PRESTON &amp;<br>AVERY ST</p>
      <p class="site-suburb">WESTMERE</p>
      <p class="site-number">#872</p>
    </div>

    <ul class="contact-list">
      <li>PO Box 4218 Greyfield
        <svg viewBox="0 0 10 10"><path d="M5 0 10 5H8.5V10H6V7H4V10H1.5V5H0Z"/></svg></li>
      <li>NSW 2190 <span class="spacer"></span></li>
      <li>0400 118 276
        <svg viewBox="0 0 10 10"><path d="M3 0H7A1 1 0 0 1 8 1V9A1 1 0 0 1 7 10H3A1 1 0 0 1 2 9V1A1 1 0 0 1 3 0ZM3 1.5V8H7V1.5Z"/></svg></li>
      <li>office@kestrelcivil.com.au
        <svg viewBox="0 0 10 10"><rect x="0" y="2" width="10" height="6" rx="1"/></svg></li>
      <li>www.kestrelcivil.com.au
        <svg viewBox="0 0 10 10"><circle cx="5" cy="5" r="4.2" fill="none" stroke="var(--brand-blue)" stroke-width="1.2"/><path d="M1 5H9M5 1V9" stroke="var(--brand-blue)" stroke-width="0.9"/></svg></li>
      <li>61 204 587 330 | <span class="abn-tag">ABN</span></li>
    </ul>
  </section>
  <span class="panel-label front-label">FRONT</span>

</body>
</html>
```